Lotus Leaf Kitchen Road Billboard

Road Billboard I need all of this information on it
Authentic Thai Food Bangkok Style
6.5 Miles on the right
4126 Maple Ridge Rd Otto NC
828-555-4172

```html
<!DOCTYPE html>
<html lang="en">
<head>
<meta charset="utf-8">
<title>Lotus Leaf Kitchen Road Billboard</title>
<link href="https://fonts.googleapis.com/css2?family=Alegreya:wght@500;600&family=Montserrat:wght@500;600&display=swap" rel="stylesheet">
<style>
  :root {
    --page: #d6d6d7;
    --board: #050505;
    --board-lift: #262626;
    --gold: #dcab12;
    --white: #ffffff;
    --ink: #0a0a0a;
    --flame-hot: #f39a1c;
    --flame-deep: #b3420b;
    --smoke: #1b1b1b;
  }
  html, body {
    margin: 0;
    width: 1198px;
    height: 1200px;
    overflow: hidden;
    background: var(--page);
  }
  .billboard {
    position: absolute;
    left: 39px;
    top: 436px;
    width: 1120px;
    height: 328px;
    box-shadow: 0 14px 28px rgba(0,0,0,0.28);
  }
  .billboard svg { display: block; width: 100%; height: 100%; }
  .serif { font-family: "Alegreya", Georgia, serif; }
  .sans { font-family: "Montserrat", Arial, sans-serif; }
  .headline { fill: var(--gold); font-weight: 600; font-size: 66px; letter-spacing: -1px; }
  .directions { fill: var(--white); font-weight: 500; font-size: 54px; letter-spacing: -1px; }
  .phone { fill: var(--ink); font-weight: 600; font-size: 84px; letter-spacing: 1px; }
  .address { fill: var(--white); font-weight: 600; font-size: 35px; }
  .brand-name { fill: var(--gold); font-weight: 600; font-size: 60px; letter-spacing: -0.5px; }
</style>
</head>
<body>
  <div class="billboard">
    <svg viewBox="0 0 1600 468" xmlns="http://www.w3.org/2000/svg">
      <defs>
        <radialGradient id="boardGlow" cx="0.22" cy="0.5" r="0.55">
          <stop offset="0" stop-color="var(--board-lift)"/>
          <stop offset="1" stop-color="var(--board)"/>
        </radialGradient>
        <radialGradient id="centerGlow" cx="0.6" cy="0.3" r="0.5">
          <stop offset="0" stop-color="#1e1e1e"/>
          <stop offset="1" stop-color="var(--board)"/>
        </radialGradient>
        <linearGradient id="wokFire" x1="0" y1="0" x2="1" y2="1">
          <stop offset="0" stop-color="var(--flame-hot)"/>
          <stop offset="0.35" stop-color="var(--flame-deep)"/>
          <stop offset="0.65" stop-color="var(--smoke)"/>
          <stop offset="1" stop-color="var(--flame-hot)"/>
        </linearGradient>
      </defs>

      <rect class="board-base" width="1600" height="468" fill="url(#centerGlow)"/>
      <path class="brand-panel" d="M0 0 L548 0 C640 60 690 150 690 234 C690 320 640 410 548 468 L0 468 Z" fill="url(#boardGlow)"/>

      <path class="phone-band" d="M672 290 L1298 290 L1300 392 L632 392 C652 362 666 328 672 290 Z" fill="var(--gold)"/>

      <path class="brand-crescent" d="M548 8 C650 70 702 160 698 238 C694 330 640 410 548 460 C628 400 672 324 674 238 C676 154 632 72 548 8 Z" fill="var(--gold)"/>

      <g role="img" aria-label="Photo of a flaming wok with shrimp, broccoli and noodles tossed in the air">
        <path class="dish-photo" d="M1392 0 L1600 0 L1600 468 L1392 468 C1300 420 1262 330 1262 234 C1262 140 1304 60 1392 0 Z" fill="url(#wokFire)"/>
      </g>
      <path class="photo-arc" d="M1380 2 C1290 64 1246 146 1244 234 C1242 322 1282 404 1376 466" fill="none" stroke="var(--gold)" stroke-width="9"/>

      <text class="brand-name serif" x="350" y="254" text-anchor="middle">Lotus Leaf Kitchen</text>

      <text class="headline serif" x="966" y="112" text-anchor="middle">Authentic Thai</text>
      <text class="headline serif" x="966" y="178" text-anchor="middle">Food Bangkok Style</text>
      <text class="directions serif" x="966" y="264" text-anchor="middle">6.5 Miles on the right</text>
      <text class="phone sans" x="966" y="372" text-anchor="middle">828-555-4172</text>
      <text class="address sans" x="966" y="442" text-anchor="middle">4126 Maple Ridge Rd Otto NC</text>
    </svg>
  </div>
</body>
</html>
```